Hardwood Flooring Company needs packaging design

We need a packaging design for our new product. We manufacture wood flooring and this year we are launching a new product that is high quality and superior durability and we want a design that communicate the superior quality of our product. We would like to see a nice design with colors shapes that communicates quality and fashion. The product carries warranty, so we need something like a 30 year warranty stamp on the box. Measurements of the box are 4” high (100mm) X 10” wide (250mm) x 84” long (2100mm).

Industry/Entity Type

Flooring

Requirements
Must have
• 30 Year warranty stamp
Should not have
• colors like blue or purple

```html
<!DOCTYPE html>
<html lang="en">
<head>
<meta charset="utf-8">
<title>Hardwood Flooring Box – Dieline</title>
<link rel="stylesheet" href="https://fonts.googleapis.com/css2?family=Michroma&display=swap">
<style>
  :root {
    --paper: #ffffff;
    --gold: #d1aa4e;
    --gold-edge: #c99d37;
    --gold-seam: #c29a45;
    --highlight: #fffcf6;
    --stamp: #4a4a4a;
    --stamp-ink: #f4f4f4;
  }
  html, body {
    margin: 0;
    padding: 0;
    width: 1200px;
    height: 3939px;
    overflow: hidden;
    background: var(--paper);
  }
  .dieline {
    position: relative;
    width: 1200px;
    height: 3939px;
  }
  .panel {
    position: absolute;
    top: 171px;
    height: 3597px;
    background: var(--gold);
    box-sizing: border-box;
  }
  .panel--front { left: 0; width: 428px; }
  .panel--top   { left: 599px; width: 428px; border-left: 1px solid var(--gold-seam); border-right: 1px solid var(--gold-seam); }
  .panel--side {
    background:
      radial-gradient(ellipse 75% 48% at 55% 50%, var(--highlight) 0%, rgba(253,246,232,0.75) 25%, rgba(236,214,160,0.45) 55%, rgba(209,170,78,0) 100%),
      linear-gradient(90deg, var(--gold) 0%, var(--gold) 60%, var(--gold-edge) 100%);
  }
  .panel--side-left  { left: 428px; width: 171px; }
  .panel--side-right { left: 1027px; width: 173px; }
  .flap {
    position: absolute;
    left: 599px;
    width: 428px;
    height: 171px;
    background: var(--gold);
    box-sizing: border-box;
  }
  .flap--top    { top: 0; border-bottom: 1px solid var(--gold-seam); }
  .flap--bottom { top: 3768px; border-top: 1px solid var(--gold-seam); }
  .warranty-stamp {
    position: absolute;
    left: 6px;
    top: 1747px;
    width: 420px;
    height: 420px;
  }
  .warranty-stamp text {
    font-family: "Michroma", "Arial", sans-serif;
    fill: var(--stamp-ink);
    stroke: var(--stamp-ink);
    stroke-width: 0.6;
  }
</style>
</head>
<body>
<div class="dieline">
  <div class="flap flap--top"></div>
  <div class="panel panel--front"></div>
  <div class="panel panel--side panel--side-left"></div>
  <div class="panel panel--top"></div>
  <div class="panel panel--side panel--side-right"></div>
  <div class="flap flap--bottom"></div>

  <svg class="warranty-stamp" viewBox="-100 -100 200 200" aria-label="30 years warranty stamp">
    <polygon fill="var(--stamp)" points="100,0 88.2,11.6 96.6,25.9 82.2,34.1 86.6,50 70.6,54.2 70.7,70.7 54.2,70.6 50,86.6 34.1,82.2 25.9,96.6 11.6,88.2 0,100 -11.6,88.2 -25.9,96.6 -34.1,82.2 -50,86.6 -54.2,70.6 -70.7,70.7 -70.6,54.2 -86.6,50 -82.2,34.1 -96.6,25.9 -88.2,11.6 -100,0 -88.2,-11.6 -96.6,-25.9 -82.2,-34.1 -86.6,-50 -70.6,-54.2 -70.7,-70.7 -54.2,-70.6 -50,-86.6 -34.1,-82.2 -25.9,-96.6 -11.6,-88.2 0,-100 11.6,-88.2 25.9,-96.6 34.1,-82.2 50,-86.6 54.2,-70.6 70.7,-70.7 70.6,-54.2 86.6,-50 82.2,-34.1 96.6,-25.9 88.2,-11.6"/>
    <g transform="rotate(-90)">
      <text x="3" y="-10" text-anchor="middle" textLength="122" lengthAdjust="spacingAndGlyphs"><tspan font-size="22">30 Y</tspan><tspan font-size="16">EARS</tspan></text>
      <text x="3" y="28" text-anchor="middle" textLength="150" lengthAdjust="spacingAndGlyphs"><tspan font-size="22">W</tspan><tspan font-size="16">ARRANTY</tspan></text>
    </g>
  </svg>
</div>
</body>
</html>
```